Buch-/E-Book-Cover für Autobiografie
Zielgruppe
Ich bin Autor und habe soeben meine Autobiografie verfasst. Sie handelt hauptsächlich von meiner Flagfootball Karriere und meinem Weg vom American Football Fan zum Flagfootball Weltmeister.
Ich benötige ein Design für das Cover des Buches im DIN A5 Format. Es sollte sehr edel aussehen.
Buchtitel: Nachtfalke
Untertitel: Mein Weg vom ersten Wurf zum Weltmeistertitel im Flagfootball
Aufgabenstellung
Auf der Vorderseite sollte eines der mitgeschickten Bilder, der Titel, der Untertitel des Buches und mein Name stehen. Egal, welches Foto für die Vorderseite ausgewählt wird, der Football sollte jedenfalls gut erkennbar sein.
Auf der Rückseite eine Buchbeschreibung und drei kurze Statements von Testimonials.
Auf dem Buchrücken mein Name und der Buchtitel (ohne Untertitel).
Farblich sollte sich das Design an den Farben meiner Website anlehnen (Hauptfarben Gold, Weiss, Schwarz)

```html
<!DOCTYPE html>
<html lang="de">
<head>
<meta charset="utf-8">
<title>Nachtfalke – Rückseite</title>
<link rel="stylesheet" href="https://fonts.googleapis.com/css2?family=Montserrat:wght@400&family=Poiret+One&display=swap">
<style>
  :root {
    --ink: #050505;
    --ink-soft: #1b1b1b;
    --cream: #efe5cc;
    --white: #ffffff;
    --gold: #bfae80;
  }
  * { margin: 0; padding: 0; box-sizing: border-box; }
  html, body { width: 846px; height: 1200px; overflow: hidden; background: var(--ink); }
  .back-cover {
    position: relative;
    width: 846px;
    height: 1200px;
    overflow: hidden;
    background:
      radial-gradient(ellipse at 80% 85%, #2a2a2a 0%, transparent 45%),
      radial-gradient(ellipse at 25% 70%, #1a1a1a 0%, transparent 40%),
      linear-gradient(180deg, var(--ink) 0%, #0a0a0a 55%, var(--ink-soft) 100%);
    font-family: "Montserrat", sans-serif;
    text-align: center;
  }
  .book-title {
    position: absolute;
    top: 10px; left: 0; width: 100%;
    font-family: "Poiret One", sans-serif;
    font-weight: 400;
    font-size: 98px;
    line-height: 1;
    letter-spacing: 6px;
    text-transform: uppercase;
    color: var(--cream);
  }
  .author-name {
    position: absolute;
    top: 132px; left: 0; width: 100%;
    font-size: 50px;
    line-height: 1.1;
    font-weight: 400;
    color: var(--white);
  }
  .blurb {
    position: absolute;
    top: 216px; left: 60px; width: 726px;
    font-size: 24.5px;
    line-height: 32.4px;
    color: var(--cream);
  }
  .testimonial { position: absolute; left: 0; width: 100%; }
  .testimonial-quote {
    font-size: 19.5px;
    line-height: 26px;
  }
  .testimonial-author {
    font-size: 46px;
    line-height: 1;
    font-weight: 400;
  }
  .testimonial--one { top: 453px; color: var(--white); }
  .testimonial--two { top: 616px; color: var(--cream); }
  .testimonial--two .testimonial-quote { font-size: 21px; line-height: 27px; }
  .testimonial--three { top: 790px; color: var(--white); }
  .testimonial--one .testimonial-author { margin-top: 14px; }
  .testimonial--two .testimonial-author { margin-top: 14px; }
  .testimonial--three .testimonial-author { margin-top: 14px; }
  .football-art {
    position: absolute;
    left: 275px; top: 957px;
    width: 290px; height: 217px;
    border-radius: 50%;
    transform: rotate(-28deg);
    background: radial-gradient(ellipse at 45% 45%, #c9b98d 0%, var(--gold) 70%);
  }
</style>
</head>
<body>
  <main class="back-cover">
    <h1 class="book-title">Nachtfalke</h1>
    <h2 class="author-name">Konrad Wiebke</h2>
    <p class="blurb">Lorem ipsum dolor sit amet, consetetur sadipscing elitr, sed diam nonumy eirmod tempor invidunt ut labore et dolore magna aliquyam erat, sed diam voluptua. At vero eos et accusam et justo duo dolores et ea rebum. Stet clita kasd gubergren, no sea takimata sanctus est Lorem ipsum dolor sit amet.</p>

    <figure class="testimonial testimonial--one">
      <blockquote class="testimonial-quote">“Lorem ipsum dolor sit amet, consetetur sadipscing<br>elitr, sed diam nonumy eirmod tempor invidunt<br>ut labore et dolore magna aliquyam erat, sed<br>diam voluptua.”</blockquote>
      <figcaption class="testimonial-author">Mustermann</figcaption>
    </figure>

    <figure class="testimonial testimonial--two">
      <blockquote class="testimonial-quote">“Lorem ipsum dolor sit amet, consetetur sadipscing<br>elitr, sed diam nonumy eirmod tempor invidunt<br>ut labore et dolore magna aliquyam erat, sed<br>diam voluptua.”</blockquote>
      <figcaption class="testimonial-author">Mustermann</figcaption>
    </figure>

    <figure class="testimonial testimonial--three">
      <blockquote class="testimonial-quote">“Lorem ipsum dolor sit amet, consetetur sadipscing<br>elitr, sed diam nonumy eirmod tempor invidunt<br>ut labore et dolore magna aliquyam erat, sed<br>diam voluptua.”</blockquote>
      <figcaption class="testimonial-author">Mustermann</figcaption>
    </figure>

    <div class="football-art" role="img" aria-label="Illustration eines goldenen American Footballs mit schwarzen Streifen und Naht"></div>
  </main>
</body>
</html>
```